I need a box design created for a DNA Fitness Test

I need a modern and sleek box design for a fitness test. The box needs to have our logo on it and should be clean and modern. The Box is 9 Inches Long 3 and 3/4 inches wide, and 2 inches tall. Company logo attached. The company name is cedar vitality.

Target Market(s)

Fitness

Industry/Entity Type

Fitness

Requirements
Must have
• Our logo

```html
<!DOCTYPE html>
<html lang="en">
<head>
<meta charset="utf-8">
<title>Cedar Vitality – DNA Fitness Test Box Lid</title>
<link rel="stylesheet" href="https://fonts.googleapis.com/css2?family=Montserrat:wght@700&family=Open+Sans:wght@800&display=swap">
<style>
  :root {
    --page-bg: #e9ebee;
    --navy-deep: #020a55;
    --navy-mid: #05247a;
    --glow-blue: #0a5fc0;
    --helix-blue: rgba(79, 143, 224, 0.55);
    --helix-pale: rgba(186, 218, 252, 0.85);
    --helix-faint: rgba(60, 110, 200, 0.28);
    --text-white: #ffffff;
    --accent-green: #8cc63f;
  }
  * { margin: 0; padding: 0; box-sizing: border-box; }
  html, body {
    width: 1189px;
    height: 1200px;
    overflow: hidden;
    background: var(--page-bg);
  }
  .lid-panel {
    position: absolute;
    left: 0;
    top: 338px;
    width: 1189px;
    height: 525px;
    overflow: hidden;
    background:
      radial-gradient(ellipse 340px 300px at 853px 250px, var(--glow-blue) 0%, var(--navy-mid) 45%, transparent 100%),
      var(--navy-deep);
  }
  .helix-artwork {
    position: absolute;
    left: 60px;
    top: 0;
    width: 600px;
    height: 525px;
    background:
      radial-gradient(ellipse 70px 120px at 210px 70px, var(--helix-blue) 0%, transparent 100%),
      radial-gradient(ellipse 110px 150px at 240px 200px, var(--helix-pale) 0%, var(--helix-blue) 45%, transparent 100%),
      radial-gradient(ellipse 150px 120px at 330px 330px, var(--helix-pale) 0%, var(--helix-blue) 50%, transparent 100%),
      radial-gradient(ellipse 90px 140px at 300px 460px, var(--helix-pale) 0%, var(--helix-blue) 50%, transparent 100%),
      radial-gradient(ellipse 220px 130px at 470px 470px, var(--helix-faint) 0%, transparent 100%),
      radial-gradient(ellipse 200px 320px at 180px 260px, var(--helix-faint) 0%, transparent 100%);
  }
  .brand-mark-dot {
    position: absolute;
    left: 795px;
    top: 112px;
    width: 118px;
    height: 118px;
    border-radius: 50%;
    background: var(--accent-green);
  }
  .brand-block {
    position: absolute;
    left: 653px;
    top: 276px;
    width: 400px;
    text-align: center;
    font-family: "Montserrat", sans-serif;
    font-weight: 700;
    color: var(--text-white);
  }
  .brand-name--main {
    display: block;
    font-size: 72px;
    line-height: 76px;
    letter-spacing: 6px;
    padding-left: 6px;
  }
  .brand-name--sub {
    display: block;
    font-size: 26px;
    line-height: 30px;
    letter-spacing: 16px;
    padding-left: 16px;
    margin-top: 2px;
  }
  .product-line {
    position: absolute;
    left: 653px;
    top: 456px;
    width: 400px;
    display: flex;
    align-items: center;
    justify-content: center;
    gap: 18px;
    font-family: "Open Sans", sans-serif;
    font-weight: 800;
    font-size: 30px;
    line-height: 36px;
    color: var(--text-white);
  }
  .product-line__dot {
    width: 22px;
    height: 22px;
    border-radius: 50%;
    background: var(--accent-green);
  }
</style>
</head>
<body>
  <section class="lid-panel">
    <div class="helix-artwork" role="img" aria-label="Glowing blue DNA double helix illustration sweeping down the left side"></div>

    <span class="brand-mark-dot"></span>
    <div class="brand-block">
      <span class="brand-name--main">CEDAR</span>
      <span class="brand-name--sub">VITALITY</span>
    </div>

    <p class="product-line">
      <span class="product-line__dot"></span>
      <span class="product-line__label">DNA Fitness Test</span>
      <span class="product-line__dot"></span>
    </p>
  </section>
</body>
</html>
```